LEARN Business Skills so you can Earn a good living

size of the poster is 8”x 10.75" plus 0.25" bleed.
Please leave 1 inch on the bottoum for footer
I want a design a poster that will attract people's attention.
I appreciate a creative ad however the ad should not take away from being able to clearly read the text.
-I also appreciate a simple creative ad that is not too busy.
-you can use graphics, vectors, or pictures of real people.
-however, if you use real people it should be a white male that is wearing a white shirt and look like a professional person.

Target Market(s)

Potential young business people

Industry/Entity Type

education

Requirements
Must have
• easy to read the text
Nice to have
• I would like a "creative" simple ad that is easy to be read
Should not have
• pictures of women

```html
<!DOCTYPE html>
<html lang="en">
<head>
<meta charset="utf-8">
<title>Learn It to Earn It – Business Enrichment Course</title>
<link href="https://fonts.googleapis.com/css2?family=Poppins:wght@300;400;500;600;700;800&display=swap" rel="stylesheet">
<style>
  :root {
    --ink: #1e1e1e;
    --band: #232323;
    --paper: #ffffff;
    --stage: #dcdcdc;
    --icon-disc: #6a6a6a;
    --rule: #9a9a9a;
    --partner: #1d2b7a;
  }
  * { margin: 0; padding: 0; box-sizing: border-box; }
  html, body { width: 1200px; height: 1200px; overflow: hidden; }
  body {
    background: var(--stage);
    font-family: "Poppins", sans-serif;
    color: var(--ink);
    position: relative;
  }
  .poster {
    position: absolute;
    left: 180px; top: 40px;
    width: 839px; height: 1121px;
    background: var(--paper);
    overflow: hidden;
  }
  .hero-photo {
    position: absolute; left: 0; top: 0;
    width: 839px; height: 676px;
    background:
      radial-gradient(ellipse 230px 380px at 650px 450px, rgba(60,60,64,0.5), rgba(60,60,64,0) 70%),
      linear-gradient(90deg, #ffffff 0%, #f3f3f3 35%, #e2e2e2 60%, #ebebeb 100%);
  }
  .headline { position: absolute; left: 45px; line-height: 1; white-space: nowrap; }
  .headline-learn { top: 34px; font-size: 178px; letter-spacing: -2px; }
  .headline-learn b { font-weight: 800; }
  .headline-learn span { font-weight: 300; margin-left: 2px; }
  .headline-earn { top: 201px; font-size: 96px; letter-spacing: -1px; }
  .headline-earn span { font-weight: 300; }
  .headline-earn b { font-weight: 800; }
  .headline-rule {
    position: absolute; left: 45px; top: 328px;
    width: 489px; height: 1px; background: var(--rule);
  }
  .course-title {
    position: absolute; left: 45px; top: 360px;
    font-size: 56px; font-weight: 800; line-height: 53px;
  }
  .course-meta {
    position: absolute; left: 45px;
    font-size: 29px; font-weight: 700; line-height: 1.2;
  }
  .meta-since { top: 532px; }
  .meta-mode { top: 584px; }

  .feature-band {
    position: absolute; left: 0; top: 676px;
    width: 839px; height: 329px;
    background: var(--band);
    color: var(--paper);
  }
  .feature-frame {
    position: absolute; left: 57px; top: 43px;
    width: 725px; height: 169px;
    border: 1.5px solid var(--paper);
    border-radius: 20px;
  }
  .feature-pill {
    position: absolute; left: 101px; top: 24px;
    width: 636px; height: 47px;
    background: var(--paper); color: var(--ink);
    border-radius: 24px;
    font-size: 29px; font-weight: 700;
    display: flex; align-items: center; justify-content: center;
    letter-spacing: -0.3px;
  }
  .feature-divider {
    position: absolute; top: 88px; width: 1px; height: 109px;
    background: #555;
  }
  .feature { position: absolute; top: 91px; width: 260px; text-align: center; }
  .feature-icon { display: block; margin: 0 auto; }
  .feature-label { margin-top: 8px; font-size: 20px; font-weight: 700; line-height: 30px; }
  .topics {
    position: absolute; left: 0; top: 240px; width: 839px;
    text-align: center;
    font-size: 12.5px; font-weight: 400; line-height: 15.5px;
    text-transform: uppercase;
  }

  .footer { position: absolute; left: 0; top: 1005px; width: 839px; height: 116px; }
  .org-name {
    position: absolute; left: 64px; top: 30px;
    display: flex; align-items: center; gap: 8px;
    font-size: 14px; font-weight: 500; line-height: 17px;
  }
  .org-name i {
    width: 20px; height: 20px; border-radius: 50%;
    background: var(--ink); display: block; flex: none;
  }
  .footer-divider {
    position: absolute; top: 27px; height: 46px;
    border-left: 1.5px dashed #777;
  }
  .contact { position: absolute; left: 223px; top: 20px; font-size: 14px; line-height: 20px; }
  .contact strong { font-weight: 700; }
  .contact .note { font-size: 13px; }
  .contact .note strong { font-weight: 600; }
  .partner { position: absolute; left: 657px; top: 16px; }
  .partner-intro { font-size: 14px; line-height: 18px; }
  .partner-name {
    margin-top: 8px; display: flex; align-items: center; gap: 8px;
    font-size: 13.5px; font-weight: 600; color: var(--partner); line-height: 15px;
  }
  .partner-name i { width: 18px; height: 18px; background: var(--partner); display: block; flex: none; }
</style>
</head>
<body>
<main class="poster">
  <div class="hero-photo" role="img" aria-label="Smiling professional man in a dark suit, white shirt and blue tie, seated at a desk in a bright blurred office"></div>

  <h1>
    <div class="headline headline-learn"><b>LEARN</b><span>IT</span></div>
    <div class="headline headline-earn"><span>TO </span><b>EARN</b><span> IT</span></div>
  </h1>
  <div class="headline-rule"></div>

  <h2 class="course-title">BUSINESS<br>ENRICHMENT<br>COURSE</h2>
  <p class="course-meta meta-since">Since 2005</p>
  <p class="course-meta meta-mode">In-person/Remote</p>

  <section class="feature-band">
    <div class="feature-frame"></div>
    <div class="feature-pill">A PROVEN SUCCESS OF HELPING PEOPLE</div>
    <div class="feature-divider" style="left:273px"></div>
    <div class="feature-divider" style="left:537px"></div>

    <div class="feature" style="left:35px">
      <svg class="feature-icon" width="58" height="58" viewBox="0 0 62 62">
        <circle cx="31" cy="31" r="30" fill="var(--icon-disc)"/>
        <circle cx="31" cy="28" r="11" fill="none" stroke="#fff" stroke-width="1.6"/>
        <path d="M26 33l-4 12 5-2 3 4 1-10M36 33l4 12-5-2-3 4-1-10" fill="none" stroke="#fff" stroke-width="1.4" stroke-linejoin="round"/>
        <path d="M26 28l3.5 3.5 6.5-7" fill="none" stroke="#fff" stroke-width="1.8" stroke-linecap="round"/>
      </svg>
      <p class="feature-label">Get a quality job</p>
    </div>

    <div class="feature" style="left:276px">
      <svg class="feature-icon" width="58" height="58" viewBox="0 0 62 62">
        <circle cx="31" cy="31" r="30" fill="var(--icon-disc)"/>
        <g fill="none" stroke="#fff" stroke-width="1.6">
          <rect x="17" y="36" width="5" height="8"/>
          <rect x="25" y="32" width="5" height="12"/>
          <rect x="33" y="28" width="5" height="16"/>
          <path d="M16 30l9-6 6 3 12-9M38 18h5v5" stroke-linecap="round" stroke-linejoin="round"/>
        </g>
      </svg>
      <p class="feature-label">Start/grow a business</p>
    </div>

    <div class="feature" style="left:527px">
      <svg class="feature-icon" width="58" height="58" viewBox="0 0 62 62">
        <circle cx="31" cy="31" r="30" fill="var(--icon-disc)"/>
        <g fill="none" stroke="#fff" stroke-width="1.6" stroke-linejoin="round" stroke-linecap="round">
          <rect x="22" y="30" width="22" height="12" rx="1"/>
          <circle cx="33" cy="36" r="3"/>
          <path d="M16 38h5M16 42h5M16 34h5M18 26l7-6 4 3 8-7M33 16h4v4"/>
        </g>
      </svg>
      <p class="feature-label">Increase their salary</p>
    </div>

    <p class="topics">
      Business Admiistration • Small Business Management • Finance • Investments • Computers • Accounting<br>
      Sales • Marketing • Project Management • Interviewing Skills • Business Law • Negotiation • Public Speaking<br>
      Import/Export • Information Technoloy • Distribution • Marketing • Bookkeeping • Real Estate<br>
      Health Care-Management • E-Commerce • Digital Marketing • Human Resources
    </p>
  </section>

  <footer class="footer">
    <div class="org-name"><i></i><span>Keystone<br>Career Center</span></div>
    <div class="footer-divider" style="left:194px"></div>
    <div class="contact">
      <p><strong>Call:</strong> 555 010 2400 x 212</p>
      <p><strong>Email:</strong> info@keystonecareers.org</p>
      <p class="note">Keystone is sponsored in part by the <strong>Harbor Light Foundation</strong></p>
    </div>
    <div class="footer-divider" style="left:634px"></div>
    <div class="partner">
      <p class="partner-intro">Sponsored in part</p>
      <div class="partner-name"><i></i><span>Bridgewell<br>Health Plan</span></div>
    </div>
  </footer>
</main>
</body>
</html>
```